Mother's Day Sale Banner Ad For Jewelry Site

We are looking for a designer to design a banner on our website advertising our Mother's Day Sale. I have enclosed a few pieces of jewelry we would like used in the ad. The ad size needs to be 1187 × 400. The ad should say:

Mother's Day Sale - Save 15% with Promo Code: LOVEMOM

Industry/Entity Type

Jewelry

```html
<!DOCTYPE html>
<html lang="en">
<head>
<meta charset="utf-8">
<title>Mother's Day Sale – Save 15%</title>
<link rel="stylesheet" href="https://fonts.googleapis.com/css2?family=Raleway:wght@400;500;600;700&display=swap">
<style>
  :root {
    --canvas-bg: #f5f5f3;
    --canvas-bg-edge: #ebebe8;
    --ink-navy: #3e3e66;
    --ink-plum: #8c2f5a;
    --gold-pale: #f4e7a8;
    --gold-light: #f6e27a;
    --gold-mid: #e2bf3e;
    --gold-deep: #c8920f;
    --ruby: #c23a66;
    --silver: #e4e2dc;
  }
  * { margin: 0; padding: 0; box-sizing: border-box; }
  html, body {
    width: 1200px;
    height: 404px;
    overflow: hidden;
    background: var(--canvas-bg);
  }
  .banner {
    position: relative;
    width: 1200px;
    height: 404px;
    overflow: hidden;
    background: radial-gradient(ellipse at 60% 45%, #fbfbfa 0%, var(--canvas-bg) 55%, var(--canvas-bg-edge) 100%);
    font-family: "Raleway", sans-serif;
  }
  .sale-ribbon {
    position: absolute;
    left: 0;
    top: 97px;
    width: 420px;
    height: 34px;
    background: linear-gradient(90deg, rgba(244,231,168,0) 0%, rgba(244,231,168,0.6) 30%, var(--gold-pale) 100%);
  }
  .headline {
    position: absolute;
    left: 96px;
    top: 99px;
    font-weight: 500;
    font-size: 23px;
    letter-spacing: 2.4px;
    color: var(--ink-navy);
    white-space: nowrap;
  }
  .offer {
    position: absolute;
    left: 96px;
    top: 133px;
    font-weight: 500;
    font-size: 48px;
    color: var(--ink-navy);
    white-space: nowrap;
    line-height: 1.1;
  }
  .offer .percent { color: var(--ink-plum); }
  .promo-label {
    position: absolute;
    left: 96px;
    top: 192px;
    font-weight: 500;
    font-size: 33px;
    color: var(--ink-navy);
    white-space: nowrap;
  }
  .promo-code {
    position: absolute;
    left: 80px;
    top: 243px;
    font-weight: 600;
    font-size: 64px;
    line-height: 1.2;
    letter-spacing: 2px;
    white-space: nowrap;
    background: linear-gradient(180deg, var(--gold-mid) 0%, var(--gold-light) 50%, var(--gold-deep) 51%, var(--gold-mid) 100%);
    -webkit-background-clip: text;
    background-clip: text;
    color: transparent;
  }
  .product {
    position: absolute;
    border-radius: 28px;
  }
  .product--brooch {
    left: 530px;
    top: 30px;
    width: 272px;
    height: 306px;
    background: linear-gradient(180deg, #e8cd6a 0%, #d9b640 35%, #c9446c 55%, #b83a5f 72%, #d9b640 100%);
  }
  .product--earrings {
    left: 858px;
    top: 45px;
    width: 154px;
    height: 150px;
    background: linear-gradient(160deg, #e6c556 0%, #d4a934 55%, #c8962a 100%);
  }
  .product--ring {
    left: 952px;
    top: 200px;
    width: 168px;
    height: 140px;
    background: linear-gradient(160deg, #e8cf6e 0%, var(--silver) 40%, #dcd8cd 65%, #d9b640 100%);
  }
</style>
</head>
<body>
  <main class="banner">
    <div class="sale-ribbon"></div>
    <h1 class="headline">MOTHER'S DAY SALE</h1>
    <p class="offer">Save <span class="percent">15%</span></p>
    <p class="promo-label">with Promo Code:</p>
    <p class="promo-code">LOVEMOM</p>

    <div class="product product--brooch" role="img" aria-label="Gold crab brooch set with pink rubies and blue sapphire eyes"></div>
    <div class="product product--earrings" role="img" aria-label="Pair of gold rope-textured earrings with diamond X accents"></div>
    <div class="product product--ring" role="img" aria-label="Gold and white gold openwork lace band ring"></div>
  </main>
</body>
</html>
```